AUSTRALIAN CONSULTING FIRM BUSINESS CARD - MODERN

We are wanting a modern, clean lined business card design. We are professional niche consultancy firm situated in Australia called Marlow Advisory Partners Pty Ltd.
The card should communicate professionalism and creativity and draw on our logo design (attached).
The design should be two sided, landscape orientation.
Target Market(s)
government, not for profit sector, corporate clients
Industry/Entity Type
Landscape
Requirements
Must have
- logo
no new introduced colours

```html
<!DOCTYPE html>
<html lang="en">
<head>
<meta charset="utf-8">
<title>Marlow Advisory Partners – Business Card</title>
<link rel="stylesheet" href="https://fonts.googleapis.com/css2?family=Questrial&display=swap">
<style>
  :root {
    --page-bg: #ebe8e3;
    --card-white: #f7f7f6;
    --brand-navy: #2f3b8f;
    --brand-blue: #1b86c9;
    --back-light: #0aa0db;
    --back-dark: #1c3d8e;
    --text-light: #eef6fc;
    --shadow: rgba(40, 35, 30, 0.22);
  }
  * { box-sizing: border-box; margin: 0; padding: 0; }
  html, body {
    width: 1200px;
    height: 900px;
    overflow: hidden;
    background: var(--page-bg);
    font-family: "Questrial", sans-serif;
  }
  .canvas {
    position: relative;
    width: 1200px;
    height: 900px;
  }
  .card {
    position: absolute;
    width: 560px;
    height: 320px;
    border-radius: 4px;
    box-shadow: 0 14px 30px var(--shadow), 0 2px 4px var(--shadow);
    overflow: hidden;
  }

  /* Front side */
  .card-front {
    left: 60px;
    top: 130px;
    background: var(--card-white);
  }
  .front-brand {
    position: absolute;
    left: 70px;
    top: 118px;
    display: flex;
    align-items: center;
    gap: 16px;
  }
  .brand-dot {
    width: 30px;
    height: 30px;
    border-radius: 50%;
    background: var(--brand-blue);
    flex: none;
  }
  .brand-name {
    color: var(--brand-navy);
    font-size: 24px;
    letter-spacing: 0.02em;
    text-transform: uppercase;
    line-height: 1.15;
  }
  .front-web {
    position: absolute;
    right: 60px;
    bottom: 54px;
    color: var(--brand-blue);
    font-size: 16px;
    letter-spacing: 0.03em;
  }

  /* Back side */
  .card-back {
    left: 580px;
    top: 470px;
    background: linear-gradient(35deg, var(--back-light) 0%, #0b7dc6 50%, var(--back-dark) 100%);
    color: var(--text-light);
  }
  .back-details {
    position: absolute;
    left: 40px;
    top: 70px;
  }
  .person-name {
    font-size: 24px;
    letter-spacing: 0.04em;
    text-transform: uppercase;
    font-weight: 400;
  }
  .person-role {
    font-size: 17px;
    margin-top: 2px;
  }
  .contact-list {
    list-style: none;
    margin-top: 26px;
    font-size: 16px;
    line-height: 1.45;
  }
  .contact-label {
    display: inline-block;
    width: 22px;
    font-weight: 700;
  }
  .address {
    margin-top: 24px;
    font-size: 16px;
    line-height: 1.45;
    font-style: normal;
  }
</style>
</head>
<body>
  <main class="canvas">
    <section class="card card-front" aria-label="Business card front">
      <div class="front-brand">
        <span class="brand-dot" aria-hidden="true"></span>
        <span class="brand-name">Marlow Advisory<br>Partners Pty Ltd</span>
      </div>
      <p class="front-web">www.marlowadvisory.com</p>
    </section>

    <section class="card card-back" aria-label="Business card back">
      <div class="back-details">
        <h1 class="person-name">Elena Hartley</h1>
        <p class="person-role">Operation manager</p>
        <ul class="contact-list">
          <li><span class="contact-label">T</span>+1 646 555 0142</li>
          <li><span class="contact-label">F</span>+61 402 555 017</li>
          <li><span class="contact-label"></span>name@marlowadvisory.com</li>
        </ul>
        <address class="address">
          Avenue des Palmiers - Rive Haute,<br>
          BP 210 - City, Country
        </address>
      </div>
    </section>
  </main>
</body>
</html>
```